The Wellness Barn Business Card

Info for the front..... (in whichever order and layout looks best)
Carla Penhallow
Physiotherapist
4/37 Upper Creekbank Rd
Tallowbrook
QLD 4712
0462305178
carlapenhallow57@mailbox.example
www.thewellnessbarn.example.au
on the back I would like to be able to write appointments so probably just that heading with lines.
I like a sort of rustic style but mostly professional, colours in naturals, beige, brown, green etc. I dont mind if the logo colour is changed slightly to suit.

```html
<!DOCTYPE html>
<html lang="en">
<head>
<meta charset="utf-8">
<title>The Wellness Barn – Business Card</title>
<link rel="stylesheet" href="https://fonts.googleapis.com/css2?family=Barlow+Condensed:wght@300;400;600;700&display=swap">
<style>
  :root {
    --backdrop: #c8c8c8;
    --paper: #ffffff;
    --front-green: #1f4f10;
    --front-orange: #c2650a;
    --front-yellow: #fbbf16;
    --back-gold: #d49a12;
    --back-brown: #9a5205;
    --back-green: #1a3d0b;
    --ink: #1d1d1d;
    --rule: #8a8a8a;
  }
  * { margin: 0; padding: 0; box-sizing: border-box; }
  html, body { width: 977px; height: 1200px; overflow: hidden; background: var(--backdrop); }
  body { position: relative; font-family: "Barlow Condensed", sans-serif; }

  .card { position: absolute; left: 110px; width: 757px; height: 456px; background: var(--paper); overflow: hidden; }
  .card--front { top: 98px; }
  .card--back { top: 641px; }
  .band { position: absolute; top: 0; height: 100%; }

  /* front */
  .card--front .band--yellow { left: 387px; width: 17px; background: var(--front-yellow); }
  .card--front .band--orange { left: 404px; width: 31px; background: var(--front-orange); }
  .card--front .band--green { left: 435px; right: 0; background: var(--front-green); }
  .contact-panel {
    position: absolute; left: 387px; top: 43px; width: 324px; height: 371px;
    background: var(--paper); border-radius: 0 41px 41px 0;
  }
  .brand-name {
    position: absolute; left: 65px; top: 115px; width: 284px; height: 229px;
    display: flex; align-items: center; justify-content: center; text-align: center;
    color: var(--front-green); font-weight: 700; font-size: 60px; line-height: 0.95;
  }
  .person { position: absolute; left: 48px; top: 14px; }
  .person__name { color: var(--front-orange); font-weight: 600; font-size: 25px; line-height: 1.2; }
  .person__role { color: var(--ink); font-weight: 300; font-size: 19px; line-height: 1.1; }
  .contacts { position: absolute; left: 45px; top: 173px; list-style: none; }
  .contacts li {
    display: flex; align-items: flex-start; gap: 7px;
    color: var(--ink); font-weight: 300; font-size: 18.5px; line-height: 25px; margin-bottom: 9px;
  }
  .contacts svg { width: 15px; height: 15px; margin-top: 5px; flex: none; fill: none; stroke: var(--front-orange); stroke-width: 1.6; stroke-linecap: round; stroke-linejoin: round; }
  .contacts .email { letter-spacing: -0.2px; }

  /* back */
  .card--back .band--gold { left: 0; width: 412px; background: var(--back-gold); }
  .card--back .band--brown { left: 412px; width: 30px; background: var(--back-brown); }
  .card--back .band--green { left: 442px; right: 0; background: var(--back-green); }
  .appointment-panel {
    position: absolute; left: 45px; top: 43px; width: 666px; height: 371px;
    background: var(--paper); border-radius: 41px;
  }
  .write-line { position: absolute; left: 45px; width: 572px; height: 1px; background: var(--rule); }
</style>
</head>
<body>

<section class="card card--front" aria-label="Business card front">
  <div class="band band--yellow"></div>
  <div class="band band--orange"></div>
  <div class="band band--green"></div>

  <div class="brand-name">The<br>Wellness<br>Barn</div>

  <div class="contact-panel">
    <div class="person">
      <p class="person__name">Carla Penhallow</p>
      <p class="person__role">Physiotherapist</p>
    </div>
    <ul class="contacts">
      <li>
        <svg viewBox="0 0 16 16"><path d="M8 14.5s4.5-4.4 4.5-8A4.5 4.5 0 0 0 3.5 6.5c0 3.6 4.5 8 4.5 8z"/><circle cx="8" cy="6.5" r="1.6"/></svg>
        <span>4/37 Upper Creekbank Rd<br>Tallowbrook QLD 4712</span>
      </li>
      <li>
        <svg viewBox="0 0 16 16"><path d="M3 2.5l2.5-.5 1.3 3-1.6 1.2a8 8 0 0 0 4.6 4.6l1.2-1.6 3 1.3-.5 2.5C8 13.5 2.5 8 3 2.5z"/><path d="M10 2.5a4 4 0 0 1 3.5 3.5M10 5a1.6 1.6 0 0 1 1 1"/></svg>
        <span>0462305178</span>
      </li>
      <li>
        <svg viewBox="0 0 16 16"><rect x="1.5" y="3.5" width="13" height="9" rx="1"/><path d="M5 7l3 2.2L11 7"/></svg>
        <span class="email">carlapenhallow57@mailbox.example</span>
      </li>
      <li>
        <svg viewBox="0 0 16 16"><circle cx="8" cy="8" r="6.3"/><path d="M1.7 8h12.6M8 1.7c-3 3.5-3 9 0 12.6M8 1.7c3 3.5 3 9 0 12.6"/></svg>
        <span>www.thewellnessbarn.example.au</span>
      </li>
    </ul>
  </div>
</section>

<section class="card card--back" aria-label="Business card back">
  <div class="band band--gold"></div>
  <div class="band band--brown"></div>
  <div class="band band--green"></div>
  <div class="appointment-panel">
    <div class="write-line" style="top:69px"></div>
    <div class="write-line" style="top:131px"></div>
    <div class="write-line" style="top:191px"></div>
    <div class="write-line" style="top:253px"></div>
    <div class="write-line" style="top:313px"></div>
  </div>
</section>

</body>
</html>
```